Brookmere Roofing Business Card

This is my current business card. But I’d like to make some changes. Somewhere on the card I’d like to list some of the services we offer. Maybe on the back? But I’d still like to keep the red. White and black modern look.

-residential & commercial roofing
-Roof Repairs & Maintenance
-Storm Damage & Insurance Claims specialist
-Christmas Lights and permanent Christmas lights
Fencing. Windows. Gutters. Siding. Sheetrock, painting.

```html
<!DOCTYPE html>
<html lang="en">
<head>
<meta charset="utf-8">
<title>Brookmere Roofing Business Card</title>
<link href="https://fonts.googleapis.com/css2?family=Michroma&family=Open+Sans:wght@400;600&family=Oswald:wght@400;500&display=swap" rel="stylesheet">
<style>
  :root {
    --stage: #3b3b3d;
    --card-black: #0b0b0b;
    --brand-red: #e0262b;
    --deep-red: #7a0f12;
    --white: #ffffff;
    --rule: #5a5a5a;
    --soft-grey: #d9d9d9;
  }
  * { box-sizing: border-box; margin: 0; padding: 0; }
  html, body { width: 1200px; height: 1200px; overflow: hidden; }
  body { background: var(--stage); position: relative; font-family: "Open Sans", sans-serif; }

  .card {
    position: absolute;
    left: 120px;
    width: 960px;
    height: 548px;
    border-radius: 36px;
    overflow: hidden;
    box-shadow: 0 18px 40px rgba(0,0,0,0.45);
  }
  .card--front { top: 36px; background: var(--card-black); color: var(--white); }
  .card--back { top: 616px; }

  /* front */
  .contact { position: absolute; left: 64px; top: 112px; width: 420px; }
  .holder-name { font-family: "Michroma", sans-serif; font-size: 34px; letter-spacing: 1px; line-height: 1.1; white-space: nowrap; }
  .holder-name .first { color: var(--brand-red); }
  .holder-role { font-size: 19px; margin-top: 8px; letter-spacing: 0.5px; }
  .holder-role .accent { color: var(--brand-red); }
  .contact-list { list-style: none; margin-top: 22px; }
  .contact-list li { display: flex; align-items: center; gap: 12px; font-size: 19px; letter-spacing: 1.5px; margin-bottom: 10px; }
  .contact-list svg { width: 20px; height: 20px; flex: none; }

  .brand-lockup { position: absolute; left: 560px; top: 92px; width: 340px; text-align: center; }
  .brand-lockup .mark { width: 110px; height: 110px; border-radius: 50%; background: var(--brand-red); border: 5px solid var(--white); margin: 0 auto 18px; }
  .brand-name { font-family: "Michroma", sans-serif; color: var(--white); font-size: 26px; line-height: 1.3; letter-spacing: 1px; }

  .divider { position: absolute; height: 1px; background: var(--rule); }
  .divider--left { left: 64px; top: 340px; width: 400px; }
  .divider--right { left: 540px; top: 340px; width: 370px; }

  .services { position: absolute; list-style: none; font-family: "Oswald", sans-serif; text-transform: uppercase; font-size: 16px; line-height: 1.55; letter-spacing: 0.3px; }
  .services li::before { content: "• "; color: var(--brand-red); }
  .services--left { left: 64px; top: 362px; }
  .services--right { left: 540px; top: 362px; width: 380px; }

  .tartan-strip {
    position: absolute; left: 0; bottom: 0; width: 100%; height: 44px;
    background: linear-gradient(90deg, var(--deep-red), var(--brand-red) 45%, #2a0a0b 70%, var(--brand-red));
  }

  /* back */
  .tartan-field {
    position: absolute; inset: 0;
    background:
      linear-gradient(180deg, rgba(0,0,0,0) 0%, rgba(0,0,0,0.35) 100%),
      linear-gradient(135deg, var(--brand-red) 0%, var(--deep-red) 35%, #1a0506 55%, var(--brand-red) 78%, var(--deep-red) 100%);
  }
  .back-lockup { position: absolute; inset: 0; display: flex; flex-direction: column; align-items: center; justify-content: center; }
  .back-lockup .mark { width: 180px; height: 180px; border-radius: 50%; background: var(--brand-red); border: 7px solid var(--white); margin-bottom: 26px; }
  .back-lockup .brand-name { font-size: 44px; text-align: center; line-height: 1.25; }
</style>
</head>
<body>

<section class="card card--front">
  <div class="contact">
    <h1 class="holder-name"><span class="first">DANA</span> WHITFIELD</h1>
    <p class="holder-role">Roofing contractor in <span class="accent">Texas</span></p>
    <ul class="contact-list">
      <li>
        <svg viewBox="0 0 24 24" aria-hidden="true"><path fill="#e0262b" d="M6.6 10.8a15 15 0 0 0 6.6 6.6l2.2-2.2a1 1 0 0 1 1-.25 11.4 11.4 0 0 0 3.6.57 1 1 0 0 1 1 1V20a1 1 0 0 1-1 1A17 17 0 0 1 3 4a1 1 0 0 1 1-1h3.5a1 1 0 0 1 1 1c0 1.25.2 2.45.57 3.6a1 1 0 0 1-.25 1z"/></svg>
        555-014-2290
      </li>
      <li>
        <svg viewBox="0 0 24 24" aria-hidden="true"><rect x="2" y="5" width="20" height="14" fill="#e0262b"/><path d="M2 5l10 8 10-8" fill="none" stroke="#0b0b0b" stroke-width="1.8"/></svg>
        dana@brookmereroofing.co
      </li>
      <li>
        <svg viewBox="0 0 24 24" aria-hidden="true"><circle cx="12" cy="12" r="9" fill="none" stroke="#e0262b" stroke-width="2"/><path d="M3 12h18M12 3c3 3 3 15 0 18M12 3c-3 3-3 15 0 18" fill="none" stroke="#e0262b" stroke-width="1.6"/></svg>
        www.brookmereroofing.co
      </li>
    </ul>
  </div>

  <div class="brand-lockup">
    <div class="mark"></div>
    <p class="brand-name">BROOKMERE<br>ROOFING CO.</p>
  </div>

  <div class="divider divider--left"></div>
  <div class="divider divider--right"></div>

  <ul class="services services--left">
    <li>Residential &amp; Commercial Roofing</li>
    <li>Roof Repairs &amp; Maintenance</li>
    <li>Storm Damage &amp; Insurance Claims Specialist</li>
  </ul>
  <ul class="services services--right">
    <li>Christmas Lights and Permanent Christmas Lights</li>
    <li>Fencing • Windows • Gutters</li>
    <li>Siding • Sheetrock • Painting.</li>
  </ul>

  <div class="tartan-strip" role="img" aria-label="Red, black and white tartan plaid band"></div>
</section>

<section class="card card--back">
  <div class="tartan-field" role="img" aria-label="Red, black and white tartan plaid pattern"></div>
  <div class="back-lockup">
    <div class="mark"></div>
    <p class="brand-name">BROOKMERE<br>ROOFING CO.</p>
  </div>
</section>

</body>
</html>
```